Motel Sign - Front

(21/03/12 - I've edited the brief and removing the words "garden view" its not fitting in the designs I'm getting and just want the word motel to be the focus. I have a template/vision of what I want - see the whiteboard sketch of what I'm looking for uploaded today. Definitely open to creatively, new designs and different ideas but the whiteboard design I've done should be a guideline. Keep it fresh/green/white. use the sample photos of green as inspiration. Thanks)
We are a motel set in the mountain country of Victoria - Australia. The front of the motel needs a fresh look. We recently removed a large amount of the garden to expose a brick courtyard fence which the front of the courtyard faces out to the main road. Within the courtyard fence there is a wooden frame and paneling.
We want to have a new sign created to slot into the wooden frame. (see photo) its the white component.
Its a very large and unusual shape and I want to keep it simple but need to fill the in the best way possible.
The space is 940mm high and 4940mm width.
The message of the sign is simple the word "MOTEL". I want people to be able to drive past and glance in and see we are a motel straight away. So the main purpose of the sign is to say "MOTEL".
I am open to colour use to match the space and have impact. I thought a background colour should be 'off white'. I'm open to the colours used to match your design as long as it matches the brief. Maybe a garden green for the emblem.
IN BRIEF:
1) the word "MOTEL"
2) Border/Background that ties in the garden.
The design should be centred, clean and simple, doesn't have to fill the whole space as long as its balanced and centred.
I like cursive and garden like designs for this one - as long its the word MOTEL still has impact. (OPEN TO NEW IDEAS)
I am also open to different ideas and suggestions if you feel you have a better way to take advantage of this space.
The sign will be 7-8 metres from the road itself.
NOTE: the photos show the space and the painted white in the space where the sign will go. The garden in front of this space will be completely cleared.
Motel

```html
<!DOCTYPE html>
<html lang="en">
<head>
<meta charset="utf-8">
<title>Motel Sign – Front</title>
<link rel="stylesheet" href="https://fonts.googleapis.com/css2?family=Great+Vibes&display=swap">
<style>
  :root {
    --lime-light: #b5d94a;
    --lime: #8cc63f;
    --garden-green: #3f9a2f;
    --forest-green: #1f6b28;
    --leaf-tone: #6fbf45;
    --swoosh-white: #f4faea;
    --ink-shadow: #1d3f14;
    --frame: #2d5a20;
  }
  * { margin: 0; padding: 0; box-sizing: border-box; }
  html, body {
    width: 1200px;
    height: 230px;
    overflow: hidden;
    background: #ffffff;
  }
  .sign {
    position: relative;
    width: 1200px;
    height: 230px;
    overflow: hidden;
    border: 2px solid var(--frame);
    background: linear-gradient(100deg,
      var(--lime-light) 0%,
      var(--lime) 40%,
      var(--garden-green) 70%,
      var(--forest-green) 100%);
  }
  .sign__backdrop {
    position: absolute;
    inset: 0;
    width: 100%;
    height: 100%;
  }
  .sign__title {
    position: absolute;
    left: 30px;
    top: 2px;
    font-family: "Great Vibes", cursive;
    font-weight: 400;
    font-size: 200px;
    line-height: 1;
    color: #ffffff;
    letter-spacing: 2px;
    text-shadow:
      -2px -2px 0 var(--ink-shadow),
       2px -2px 0 var(--ink-shadow),
      -2px  2px 0 var(--ink-shadow),
       2px  2px 0 var(--ink-shadow),
       5px  6px 6px rgba(0, 0, 0, 0.35);
  }
</style>
</head>
<body>
  <div class="sign">
    <svg class="sign__backdrop" viewBox="0 0 1200 230" preserveAspectRatio="none" aria-hidden="false">
      <defs>
        <linearGradient id="swooshFade" x1="0" y1="1" x2="1" y2="0">
          <stop offset="0" stop-color="var(--swoosh-white)" stop-opacity="0.9"/>
          <stop offset="1" stop-color="var(--swoosh-white)" stop-opacity="0.15"/>
        </linearGradient>
        <radialGradient id="leafTone" cx="0.55" cy="0.4" r="0.6">
          <stop offset="0" stop-color="var(--leaf-tone)" stop-opacity="0.85"/>
          <stop offset="1" stop-color="var(--leaf-tone)" stop-opacity="0"/>
        </radialGradient>
      </defs>
      <!-- light sweeping curve across the background -->
      <path class="sign__swoosh"
            d="M0 200 C 250 170, 520 120, 760 0 L 800 0 C 560 140, 300 200, 0 230 Z"
            fill="url(#swooshFade)"/>
      <path class="sign__swoosh-line"
            d="M0 215 C 280 190, 560 130, 820 0"
            fill="none" stroke="var(--swoosh-white)" stroke-opacity="0.5" stroke-width="3"/>
      <!-- leaf artwork area -->
      <g role="img" aria-label="Green leaves with water droplets">
        <ellipse cx="1020" cy="70" rx="200" ry="110" fill="url(#leafTone)"/>
        <ellipse cx="790" cy="200" rx="110" ry="60" fill="url(#leafTone)"/>
      </g>
    </svg>
    <h1 class="sign__title">Motel</h1>
  </div>
</body>
</html>
```